HVAC Van wrap design, High end commercial HVAC controls company.

Looking for a clean, professional design that still lists company services.
Some product services include programming HVAC equipment on large buildings, with an eye for energy savings (dont want any cheesy 'green' logo)
Also, Industrial or technical are words I would use to describe the desired look.

Target Market(s)

Commercial HVAC clients, commercial buildings

Industry/Entity Type

Heating, air conditioning and commercial controls (equipment programming)

Requirements
Must have
• 'cool' use of logo

```html
<!DOCTYPE html>
<html lang="en">
<head>
<meta charset="utf-8">
<title>Northgate Mechanical – Van Wrap</title>
<link rel="stylesheet" href="https://fonts.googleapis.com/css2?family=Montserrat:ital,wght@0,400;0,700;1,800&display=swap">
<style>
  :root {
    --wrap-blue: #1f7ac9;
    --wrap-blue-deep: #1462b3;
    --wrap-red: #c3222a;
    --wrap-white: #f2f3f4;
    --trim-dark: #2f3033;
    --glass: #3b3d42;
    --tyre: #232427;
    --hub: #b9bcc1;
    --stage: #e3e4e7;
  }
  html, body {
    margin: 0;
    width: 1200px;
    height: 2700px;
    overflow: hidden;
    background: var(--stage);
    font-family: "Montserrat", sans-serif;
  }
  .wrap-sheet { width: 1200px; height: 2700px; display: flex; flex-direction: column; }
  .view { display: block; width: 1200px; height: 675px; }
  .view + .view { border-top: 2px solid #d3d5d9; box-sizing: border-box; }

  .fill-blue { fill: var(--wrap-blue); }
  .fill-blue-deep { fill: var(--wrap-blue-deep); }
  .fill-red { fill: var(--wrap-red); }
  .fill-white { fill: var(--wrap-white); }
  .fill-trim { fill: var(--trim-dark); }
  .fill-glass { fill: var(--glass); }
  .fill-tyre { fill: var(--tyre); }
  .fill-hub { fill: var(--hub); }

  .brand-name { fill: var(--wrap-blue); font-weight: 400; letter-spacing: 0.04em; }
  .brand-dot { fill: var(--wrap-red); }
  .phone { fill: #fff; font-weight: 700; }
  .services { fill: #fff; font-weight: 800; font-style: italic; }
  .email { fill: #fff; font-weight: 400; }
</style>
</head>
<body>
<main class="wrap-sheet">

  <!-- Front view -->
  <svg class="view view-front" viewBox="0 0 1200 675" aria-label="Front of van wrap">
    <rect class="fill-trim" x="255" y="225" width="65" height="90" rx="14"/>
    <rect class="fill-trim" x="880" y="225" width="65" height="90" rx="14"/>
    <path class="fill-white" d="M335 90 Q340 55 400 52 L800 52 Q860 55 865 90 L880 470 L320 470 Z"/>
    <path class="fill-blue" d="M335 90 Q340 55 400 52 L800 52 Q860 55 865 90 L872 300 L800 300 L790 290 L410 290 L400 300 L328 300 Z"/>
    <rect class="fill-glass" x="360" y="105" width="480" height="175" rx="20"/>
    <polygon class="fill-red" points="410 300 440 300 470 380 450 380"/>
    <polygon class="fill-red" points="790 300 760 300 730 380 750 380"/>
    <polygon class="fill-blue-deep" points="330 300 405 300 445 380 360 380"/>
    <polygon class="fill-blue-deep" points="870 300 795 300 755 380 840 380"/>
    <text class="brand-name" x="600" y="325" font-size="26" text-anchor="middle">NORTHGATE</text>
    <text class="brand-name" x="600" y="344" font-size="11" text-anchor="middle">MECHANICAL</text>
    <rect class="fill-hub" x="340" y="335" width="70" height="50" rx="12"/>
    <rect class="fill-hub" x="790" y="335" width="70" height="50" rx="12"/>
    <rect class="fill-trim" x="425" y="360" width="350" height="110" rx="16"/>
    <path class="fill-trim" d="M305 430 L895 430 L880 560 L320 560 Z"/>
    <rect class="fill-tyre" x="305" y="530" width="75" height="85" rx="10"/>
    <rect class="fill-tyre" x="820" y="530" width="75" height="85" rx="10"/>
  </svg>

  <!-- Driver side -->
  <svg class="view view-side-left" viewBox="0 0 1200 675" aria-label="Left side of van wrap">
    <defs>
      <clipPath id="side-body-left">
        <path d="M30 330 L50 285 L170 250 L330 105 Q360 88 420 88 L1140 85 Q1168 88 1168 112 L1170 440 L30 440 Z"/>
      </clipPath>
    </defs>
    <g class="van-body">
      <g clip-path="url(#side-body-left)">
        <rect class="fill-white" x="0" y="0" width="1200" height="460"/>
        <polygon class="fill-blue" points="0 0 1200 0 1200 70 1000 96 440 195 0 290"/>
        <polygon class="fill-red" points="440 212 960 120 1000 85 1200 85 1200 95 1010 120 960 165 440 257"/>
        <polygon class="fill-red" points="300 400 560 378 560 386 300 408"/>
        <polygon class="fill-blue" points="290 428 540 419 1170 308 1170 338 540 449"/>
        <polygon class="fill-red" points="560 445 1170 338 1170 460 560 460"/>
        <polygon class="fill-blue" points="840 437 1170 379 1170 384 840 442"/>
      </g>
      <path class="fill-glass" d="M200 258 L335 130 Q345 122 360 122 L440 122 L440 260 Z"/>
      <rect class="fill-trim" x="30" y="440" width="1140" height="45" rx="8"/>
      <polygon class="fill-blue" points="470 470 560 470 540 490 450 490"/>
      <polygon class="fill-red" points="580 470 880 470 860 490 560 490"/>
      <circle class="fill-tyre" cx="225" cy="495" r="64"/><circle class="fill-hub" cx="225" cy="495" r="36"/>
      <circle class="fill-tyre" cx="965" cy="495" r="64"/><circle class="fill-hub" cx="965" cy="495" r="36"/>
    </g>
    <text class="phone" font-size="32" transform="translate(480 238) rotate(-10)">☏ +1 833-555-0142</text>
    <g class="wordmark" transform="translate(550 345) rotate(-10)">
      <circle class="brand-dot" cx="-26" cy="-27" r="13"/>
      <text class="brand-name" x="0" y="0" font-size="74" textLength="555" lengthAdjust="spacing">NORTHGATE</text>
    </g>
    <text class="brand-name" font-size="36" textLength="290" lengthAdjust="spacing" transform="translate(700 385) rotate(-10)">MECHANICAL</text>
    <text class="services" font-size="14" textLength="540" lengthAdjust="spacing" transform="translate(590 430) rotate(-10)">Heating | Air Conditioning | Commercial Controls | Equipment Programming</text>
    <text class="email" font-size="21" transform="translate(830 426) rotate(-10)">info@northgatemech.com</text>
  </svg>

  <!-- Rear view -->
  <svg class="view view-rear" viewBox="0 0 1200 675" aria-label="Rear of van wrap">
    <rect class="fill-white" x="310" y="45" width="520" height="500" rx="30"/>
    <rect class="fill-red" x="505" y="45" width="120" height="12" rx="6"/>
    <rect class="fill-blue" x="310" y="270" width="520" height="38"/>
    <rect class="fill-red" x="310" y="308" width="520" height="170"/>
    <polygon class="fill-white" points="510 330 830 320 830 330 510 340"/>
    <polygon class="fill-blue" points="565 345 830 338 830 350 565 355"/>
    <polygon class="fill-blue" points="430 448 830 440 830 478 420 478"/>
    <line x1="565" y1="60" x2="565" y2="545" stroke="#c9cbcf" stroke-width="2"/>
    <circle class="brand-dot" cx="366" cy="143" r="12"/>
    <text class="brand-name" x="580" y="162" font-size="52" text-anchor="middle">NORTHGATE</text>
    <text class="brand-name" x="570" y="222" font-size="26" text-anchor="middle">MECHANICAL</text>
    <text class="services" x="565" y="294" font-size="12" text-anchor="middle">Heating | Air Conditioning | Commercial Controls | Equipment Programming</text>
    <text class="phone" x="565" y="420" font-size="34" text-anchor="middle">☏ +1 833-555-0142</text>
    <text class="email" x="565" y="468" font-size="16" text-anchor="middle">info@northgatemech.com</text>
    <rect class="fill-trim" x="300" y="478" width="540" height="80" rx="10"/>
    <rect class="fill-tyre" x="330" y="555" width="60" height="35" rx="6"/>
    <rect class="fill-tyre" x="750" y="555" width="60" height="35" rx="6"/>
  </svg>

  <!-- Passenger side -->
  <svg class="view view-side-right" viewBox="0 0 1200 675" aria-label="Right side of van wrap">
    <defs>
      <clipPath id="side-body-right">
        <path d="M30 330 L50 285 L170 250 L330 105 Q360 88 420 88 L1140 85 Q1168 88 1168 112 L1170 440 L30 440 Z"/>
      </clipPath>
    </defs>
    <g class="van-body" transform="translate(1200 0) scale(-1 1)">
      <g clip-path="url(#side-body-right)">
        <rect class="fill-white" x="0" y="0" width="1200" height="460"/>
        <polygon class="fill-blue" points="0 0 1200 0 1200 70 1000 96 440 195 0 290"/>
        <polygon class="fill-red" points="440 212 960 120 1000 85 1200 85 1200 95 1010 120 960 165 440 257"/>
        <polygon class="fill-red" points="300 400 560 378 560 386 300 408"/>
        <polygon class="fill-blue" points="290 428 540 419 1170 308 1170 338 540 449"/>
        <polygon class="fill-red" points="560 445 1170 338 1170 460 560 460"/>
        <polygon class="fill-blue" points="840 437 1170 379 1170 384 840 442"/>
      </g>
      <path class="fill-glass" d="M200 258 L335 130 Q345 122 360 122 L440 122 L440 260 Z"/>
      <rect class="fill-trim" x="30" y="440" width="1140" height="45" rx="8"/>
      <polygon class="fill-blue" points="470 470 560 470 540 490 450 490"/>
      <polygon class="fill-red" points="580 470 880 470 860 490 560 490"/>
      <circle class="fill-tyre" cx="225" cy="495" r="64"/><circle class="fill-hub" cx="225" cy="495" r="36"/>
      <circle class="fill-tyre" cx="965" cy="495" r="64"/><circle class="fill-hub" cx="965" cy="495" r="36"/>
    </g>
    <text class="phone" font-size="32" transform="translate(385 179) rotate(10)">☏ +1 833-555-0142</text>
    <g class="wordmark" transform="translate(99 248) rotate(10)">
      <circle class="brand-dot" cx="-26" cy="-27" r="13"/>
      <text class="brand-name" x="0" y="0" font-size="74" textLength="555" lengthAdjust="spacing">NORTHGATE</text>
    </g>
    <text class="brand-name" font-size="36" textLength="290" lengthAdjust="spacing" transform="translate(214 335) rotate(10)">MECHANICAL</text>
    <text class="services" font-size="14" textLength="540" lengthAdjust="spacing" transform="translate(73 337) rotate(10)">Heating | Air Conditioning | Commercial Controls | Equipment Programming</text>
    <text class="email" font-size="21" transform="translate(102 379) rotate(10)">info@northgatemech.com</text>
  </svg>

</main>
</body>
</html>
```